New York IT Service, Technology & Security Co.

need a new business card design for our Technology & Security Company. We are a Computer Networking Company, Security Camera Installers, Phone Systems.

Target Market(s)

Construction, Medical, Law Offices, Accounting, Retail etc.

Industry/Entity Type

Information Technology

Logo is attached, colors are Blue, Red, Black. Blue for Technology & Red is for Security Cameras, Access Control, Alarm Systems

Colors
fbed22
ec1f27
0555a3
ffffff

Requirements
Must have
• Pictures or Icons for
• For Technology:
• Computer, Network, Phone System, Copier, TV, Cabling
• For Security:
• Video Surveillance, Access Control, Intercom, Fire Alarm, Burglar Alarm, Time Clock

```html
<!DOCTYPE html>
<html lang="en">
<head>
<meta charset="utf-8">
<title>Business Card</title>
<link rel="stylesheet" href="https://fonts.googleapis.com/css2?family=Source+Sans+3:wght@400&display=swap">
<style>
  :root {
    --bg: #5f6369;
    --tile: #76787b;
    --tile-edge: #8c8e91;
    --panel: rgba(140, 142, 146, 0.75);
    --brand-yellow: #fbed22;
    --brand-red: #ec1f27;
    --brand-blue: #0555a3;
    --brand-white: #ffffff;
    --text: #fbf8e6;
    --icon: #fbed22;
  }
  * { margin: 0; padding: 0; box-sizing: border-box; }
  html, body { width: 1200px; height: 686px; overflow: hidden; background: var(--bg); }
  .card {
    position: relative;
    width: 1200px;
    height: 686px;
    overflow: hidden;
    font-family: "Source Sans 3", "Myriad Pro", sans-serif;
  }
  .backdrop {
    position: absolute;
    inset: 0;
    background: radial-gradient(ellipse at 30% 40%, #676b71 0%, var(--bg) 70%);
  }
  .tile {
    position: absolute;
    background: var(--tile);
    border: 1px solid var(--tile-edge);
    box-shadow: -14px 16px 26px rgba(30, 33, 38, 0.55);
  }
  .tile--small  { left: 337px;  top: 119px; width: 225px; height: 229px; border-radius: 20px; }
  .tile--top    { left: 591px;  top: -12px; width: 407px; height: 359px; border-radius: 25px; }
  .tile--edge-top { left: 1026px; top: -12px; width: 200px; height: 398px; border-radius: 25px; }
  .tile--large  { left: 360px;  top: 377px; width: 638px; height: 340px; border-radius: 34px; }
  .tile--edge-bottom { left: 1026px; top: 417px; width: 200px; height: 300px; border-radius: 25px; }

  .service-icons {
    position: absolute;
    fill: none;
    stroke-width: 4;
    stroke-linecap: round;
    stroke-linejoin: round;
  }
  .service-icons--technology { left: 636px; top: 60px; width: 318px; height: 220px; stroke: var(--brand-blue); }
  .service-icons--security   { left: 612px; top: 425px; width: 360px; height: 220px; stroke: var(--brand-red); }
  .service-icons .dot { fill: currentColor; stroke: none; }
  .service-icons--technology .dot { fill: var(--brand-blue); }
  .service-icons--security .dot { fill: var(--brand-red); }

  .contact-panel {
    position: absolute;
    left: 105px; top: 377px;
    width: 226px; height: 229px;
    border-radius: 14px;
    background: var(--panel);
    box-shadow: -10px 14px 24px rgba(30, 33, 38, 0.5);
  }
  .brand-square {
    position: absolute;
    left: 138px;
    width: 65px; height: 65px;
    border-radius: 6px;
    box-shadow: 0 2px 4px rgba(0,0,0,0.35);
  }
  .brand-square--yellow {
    top: 379px;
    background: linear-gradient(135deg, #fff9b0 0%, var(--brand-yellow) 40%, #c9b80e 60%, var(--brand-yellow) 80%, #fff9b0 100%);
  }
  .brand-square--red {
    top: 459px;
    background: linear-gradient(135deg, #ff7a7f 0%, var(--brand-red) 40%, #a8121a 60%, var(--brand-red) 80%, #ff7a7f 100%);
  }
  .brand-square--blue {
    top: 541px;
    background: linear-gradient(135deg, #5a9ad8 0%, var(--brand-blue) 40%, #03386b 60%, var(--brand-blue) 80%, #5a9ad8 100%);
  }
  .name {
    position: absolute;
    left: 234px; top: 380px;
    font-size: 39px;
    line-height: 1;
    color: var(--text);
    white-space: nowrap;
  }
  .contact-line {
    position: absolute;
    left: 232px;
    display: flex;
    align-items: center;
    gap: 18px;
    font-size: 32px;
    line-height: 1;
    color: var(--text);
    white-space: nowrap;
  }
  .contact-line svg { width: 24px; height: 24px; flex: none; fill: var(--icon); }
  .contact-line--email  { top: 435px; }
  .contact-line--mobile { top: 480px; }
  .contact-line--phone  { top: 526px; }
  .contact-line--web    { top: 572px; }
</style>
</head>
<body>
<div class="card">
  <div class="backdrop" role="img" aria-label="Dark grey background with a faint floral damask pattern"></div>

  <div class="tile tile--small"></div>
  <div class="tile tile--top"></div>
  <div class="tile tile--edge-top"></div>
  <div class="tile tile--large"></div>
  <div class="tile tile--edge-bottom"></div>

  <svg class="service-icons service-icons--technology" viewBox="0 0 318 220" role="img" aria-label="Technology services: computer, network, phone system, copier, TV, cabling">
    <g transform="translate(21 20)">
      <rect x="4" y="8" width="56" height="36" rx="3"/><path d="M22 56h20M32 44v12"/>
    </g>
    <g transform="translate(127 20)">
      <circle cx="32" cy="10" r="7"/><circle cx="10" cy="52" r="7"/><circle cx="54" cy="52" r="7"/>
      <path d="M28 16 14 46M36 16l14 30M17 52h30"/>
    </g>
    <g transform="translate(233 20)">
      <path d="M8 22q24-16 48 0v6H46v-4H18v4H8z"/><rect x="8" y="32" width="48" height="26" rx="4"/>
      <circle class="dot" cx="22" cy="40" r="2.5"/><circle class="dot" cx="32" cy="40" r="2.5"/><circle class="dot" cx="42" cy="40" r="2.5"/>
      <circle class="dot" cx="22" cy="50" r="2.5"/><circle class="dot" cx="32" cy="50" r="2.5"/><circle class="dot" cx="42" cy="50" r="2.5"/>
    </g>
    <g transform="translate(21 130)">
      <path d="M14 22V8h36v14"/><rect x="6" y="22" width="52" height="24" rx="3"/><rect x="14" y="46" width="36" height="12"/>
    </g>
    <g transform="translate(127 130)">
      <rect x="4" y="8" width="56" height="36" rx="3"/><path d="M18 58l6-14M46 58l-6-14"/>
    </g>
    <g transform="translate(233 130)">
      <path d="M6 54c22 0 18-38 40-38"/><rect x="44" y="8" width="12" height="18" rx="2"/><path d="M56 12h5M56 22h5"/>
    </g>
  </svg>

  <svg class="service-icons service-icons--security" viewBox="0 0 360 220" role="img" aria-label="Security services: video surveillance, access control, intercom, fire alarm, burglar alarm, time clock">
    <g transform="translate(28 20)">
      <path d="M6 12l42 10-4 16L2 28z"/><path d="M30 34v12H14M14 38v18"/>
    </g>
    <g transform="translate(148 20)">
      <rect x="16" y="2" width="32" height="58" rx="4"/>
      <circle class="dot" cx="26" cy="24" r="2.5"/><circle class="dot" cx="38" cy="24" r="2.5"/>
      <circle class="dot" cx="26" cy="34" r="2.5"/><circle class="dot" cx="38" cy="34" r="2.5"/>
      <circle class="dot" cx="26" cy="44" r="2.5"/><circle class="dot" cx="38" cy="44" r="2.5"/>
      <path d="M24 12h16"/>
    </g>
    <g transform="translate(268 20)">
      <rect x="12" y="2" width="40" height="58" rx="4"/><path d="M22 14h20M22 22h20M22 30h20"/><circle cx="32" cy="46" r="6"/>
    </g>
    <g transform="translate(28 134)">
      <path d="M32 4c10 14 20 22 20 36a20 20 0 0 1-40 0c0-10 8-16 10-24 4 8 8 10 10 12 0-8 0-16 0-24z"/>
    </g>
    <g transform="translate(148 134)">
      <path d="M12 46c4-6 4-14 4-22a16 16 0 0 1 32 0c0 8 0 16 4 22z"/><path d="M26 52a6 6 0 0 0 12 0"/><path d="M4 14q-4 10 0 20M60 14q4 10 0 20"/>
    </g>
    <g transform="translate(268 134)">
      <circle cx="32" cy="32" r="26"/><path d="M32 14v18l12 8"/>
    </g>
  </svg>

  <div class="contact-panel"></div>
  <div class="brand-square brand-square--yellow"></div>
  <div class="brand-square brand-square--red"></div>
  <div class="brand-square brand-square--blue"></div>

  <div class="name">John Doe</div>

  <div class="contact-line contact-line--email">
    <svg viewBox="0 0 24 24" aria-hidden="true"><path d="M2 7h20v11H2z M2 7l10 7 10-7" fill="none" stroke="#fbed22" stroke-width="2"/></svg>
    <span>jd.kestrelnet.com</span>
  </div>
  <div class="contact-line contact-line--mobile">
    <svg viewBox="0 0 24 24" aria-hidden="true"><path d="M7 1h10a1 1 0 0 1 1 1v20a1 1 0 0 1-1 1H7a1 1 0 0 1-1-1V2a1 1 0 0 1 1-1zm1 3v7h8V4zm0 9v2h2v-2zm3 0v2h2v-2zm3 0v2h2v-2zm-6 3v2h2v-2zm3 0v2h2v-2zm3 0v2h2v-2z"/></svg>
    <span>(00) 000-000-0000</span>
  </div>
  <div class="contact-line contact-line--phone">
    <svg viewBox="0 0 24 24" aria-hidden="true"><path d="M2 8c0-2 4-4 10-4s10 2 10 4v2h-5V8H7v2H2zM5 12h14l2 8H3zm7 2a2.5 2.5 0 1 0 0 5 2.5 2.5 0 0 0 0-5z"/></svg>
    <span>000-0000</span>
  </div>
  <div class="contact-line contact-line--web">
    <svg viewBox="0 0 24 24" aria-hidden="true"><circle cx="12" cy="12" r="10" fill="none" stroke="#fbed22" stroke-width="1.6"/><circle cx="13" cy="7" r="1.4"/><path d="M11 10h3l-1.5 8h-2z"/></svg>
    <span>http://kestrelnet.com</span>
  </div>
</div>
</body>
</html>
```